Tango Holiday Website Needs a Header Design

I'm looking for a talented designer to create an attractive header for my website: http://brightmerengue.de/. I only want a Header Design. The website and everything else should stay the same.
We will be offering vacations for people who want to come to Tenerife to learn and dance Argentine tango. There will be lessons during the day and dancing during the evening. Tenerife is a warm and sunny destination.
The header should blend in well with the background and the images. The current dimentions fo the header is 960 x 160 pixels.
I like the design on a similar website: http://velosacumbia.de/.
Here are some images on google for tango holiday that might help: http://qlnk.to/7kRw41P
I'm flexible with colours and am looking forward to your suggestions.
Tango dancers between the ages of 40 and 65

```html
<!DOCTYPE html>
<html lang="en">
<head>
<meta charset="UTF-8">
<title>Bright Merengue — Tango Holidays in Tenerife</title>
<link rel="stylesheet" href="https://fonts.googleapis.com/css2?family=Cormorant+Garamond:wght@500&display=swap">
<style>
  :root {
    --sea-pale: #e6f7fa;
    --sea-light: #bfeaf1;
    --sea-mid: #8fdbe6;
    --sky: #dceef3;
    --pool: #5ccfd9;
    --pool-deep: #3fb9c6;
    --deck: #c9a58a;
    --ink: #1c1c1c;
    --crimson: #a3162a;
  }
  html, body {
    margin: 0;
    padding: 0;
    width: 1200px;
    height: 200px;
    overflow: hidden;
    background: #ffffff;
  }
  .site-header {
    position: relative;
    width: 1200px;
    height: 200px;
    overflow: hidden;
    background: linear-gradient(90deg, var(--sea-pale) 0%, var(--sea-light) 35%, var(--sea-mid) 70%, var(--pool) 100%);
  }
  .hero-photo {
    position: absolute;
    top: 0;
    right: 0;
    width: 620px;
    height: 200px;
    background: linear-gradient(180deg, var(--sky) 0%, var(--sky) 18%, var(--pool) 30%, var(--pool-deep) 62%, var(--pool) 80%, var(--deck) 90%, var(--deck) 100%);
    -webkit-mask-image: linear-gradient(90deg, transparent 0%, #000 28%);
            mask-image: linear-gradient(90deg, transparent 0%, #000 28%);
  }
  .brand-name {
    position: absolute;
    left: 52px;
    top: 40px;
    margin: 0;
    font-family: "Cormorant Garamond", serif;
    font-weight: 500;
    font-size: 72px;
    line-height: 1;
    color: var(--ink);
    white-space: nowrap;
  }
  .tagline {
    position: absolute;
    left: 171px;
    top: 133px;
    margin: 0;
    font-family: "Cormorant Garamond", serif;
    font-weight: 500;
    font-size: 19px;
    line-height: 1.2;
    letter-spacing: 1px;
    text-transform: uppercase;
    color: var(--crimson);
    white-space: nowrap;
  }
</style>
</head>
<body>
  <header class="site-header">
    <div class="hero-photo" role="img" aria-label="Photo of a couple in white dancing tango beside a turquoise seaside pool in Tenerife"></div>
    <h1 class="brand-name">Bright Merengue</h1>
    <p class="tagline">Tango Holidays in Tenerife</p>
  </header>
</body>
</html>
```